FILE SETUP - BENEFITS FOR DOGS / CATS

hello ,

looking to set up a file for the printer in regards to benefits for dogs and benefits for cats.

Two Sided. Front and Back.

```html
<!DOCTYPE html>
<html lang="en">
<head>
<meta charset="utf-8">
<title>File Setup – Benefits for Dogs / Cats</title>
<link href="https://fonts.googleapis.com/css2?family=Oswald:wght@300;700&family=Barlow+Condensed:ital,wght@1,600&family=Montserrat:wght@400;700&display=swap" rel="stylesheet">
<style>
  :root{
    --board:#333333;
    --band:#4a4a4a;
    --band-text:#cfcfcf;
    --plum:#44224f;
    --lilac:#8459a6;
    --magenta:#92278f;
    --green:#7dc242;
    --orange:#f7941d;
    --sun:#f7c531;
    --lemon:#f5e51b;
    --sky:#27aae1;
    --ink:#3d1f4f;
    --navy:#2b2a6e;
    --royal:#2b3990;
    --white:#ffffff;
  }
  *{margin:0;padding:0;box-sizing:border-box}
  html,body{width:1200px;height:963px;overflow:hidden;background:var(--board)}
  .board{position:relative;width:1200px;height:963px;background:var(--board)}
  .title-band{position:absolute;left:0;top:38px;width:1200px;height:99px;background:var(--band);
    font-family:"Montserrat",sans-serif;color:var(--band-text);padding:17px 0 0 89px;font-size:29px;line-height:33px;letter-spacing:1px}
  .title-band b{font-weight:700}

  .flyer{position:absolute;top:189px;width:498px;height:706px;overflow:hidden}
  .flyer--dog{left:88.5px;background:var(--plum)}
  .flyer--cat{left:613.5px;background:var(--white)}
  .sheet{position:absolute;left:0;top:0;width:895px;height:1268px;transform:scale(0.5566);transform-origin:0 0}
  .sheet > *{position:absolute}
  .bg{left:0;top:0;width:895px;height:1268px}

  .headline{font-family:"Oswald",sans-serif;line-height:1;white-space:nowrap}
  .headline--top{font-weight:700;font-size:124px;letter-spacing:-3px;top:60px}
  .headline--line{font-weight:300;font-size:92px;letter-spacing:-2px}
  .headline--line strong{font-weight:700}
  .headline--pet{font-weight:700;font-size:218px;letter-spacing:-4px;top:372px}

  .flyer--dog .headline{left:70px}
  .flyer--dog .headline--top{color:var(--green)}
  .flyer--dog .headline--line{color:var(--white)}
  .flyer--dog .headline--pet{color:var(--orange)}
  .flyer--cat .headline{left:62px}
  .flyer--cat .headline--top{color:var(--ink)}
  .flyer--cat .headline--line{color:var(--orange)}
  .flyer--cat .headline--pet{color:var(--ink);left:376px;top:268px}
  .line-1{top:191px}
  .line-2{top:289px}

  .benefits{list-style:none;font-family:"Barlow Condensed",sans-serif;font-style:italic;font-weight:600;font-size:31px;line-height:1}
  .benefits li{position:absolute;left:0;white-space:nowrap;padding-left:44px;height:34px;display:flex;align-items:center}
  .benefits svg{position:absolute;left:0;top:2px;width:30px;height:30px}
  .flyer--dog .benefits{left:69px;top:644px;color:var(--white)}
  .flyer--cat .benefits{left:443px;top:512px;color:var(--navy)}

  .photo{border-radius:26px}
  .photo--dog-hero{left:440px;top:330px;width:400px;height:510px;border-radius:45% 45% 30% 30%;
    background:radial-gradient(ellipse at 50% 45%,#8a5230 0%,#6e3d22 45%,rgba(68,34,79,0) 72%)}
  .photo--cat-hero{left:15px;top:375px;width:405px;height:445px;border-radius:45% 45% 35% 35%;
    background:radial-gradient(ellipse at 50% 50%,#9c8a72 0%,#b9a68a 40%,rgba(255,255,255,0) 72%)}
  .photo--cats-row{left:48px;top:1016px;width:515px;height:225px;border-radius:40px 40px 10px 10px;
    background:linear-gradient(90deg,#8d8373,#a39583 25%,#d9a86c 45%,#d29454 65%,#3b3a3e 85%)}
  .frame{border:13px solid;border-radius:30px}
  .frame--yellow{left:130px;top:988px;width:330px;height:222px;border-color:var(--lemon);transform:rotate(8deg);
    background:linear-gradient(135deg,#5f7d4a,#a7b88c 45%,#d39a5a 80%)}
  .frame--blue-dog{left:514px;top:988px;width:300px;height:202px;border-color:var(--sky);transform:rotate(-8deg);
    background:linear-gradient(135deg,#9d8d6c,#6d6459 40%,#e8e2d6 75%)}
  .frame--blue-cat{left:444px;top:850px;width:330px;height:215px;border-color:var(--sky);transform:rotate(-5deg);
    background:linear-gradient(135deg,#c9c7c2,#f0ede8 40%,#d7934f 75%)}
</style>
</head>
<body>
<svg width="0" height="0" style="position:absolute" aria-hidden="true">
  <defs>
    <symbol id="paw-badge" viewBox="0 0 30 30">
      <circle cx="15" cy="15" r="14" fill="var(--badge)"/>
      <g fill="var(--pad)">
        <ellipse cx="15" cy="19" rx="5.5" ry="4.5"/>
        <circle cx="9" cy="13" r="2.2"/>
        <circle cx="12.5" cy="9.5" r="2.2"/>
        <circle cx="17.5" cy="9.5" r="2.2"/>
        <circle cx="21" cy="13" r="2.2"/>
      </g>
    </symbol>
  </defs>
</svg>

<main class="board">
  <header class="title-band">
    <div>FILE SETUP - BENEFITS FOR <b>DOGS / CATS</b></div>
    <div>FLYER FRONT BACK: <b>A5 Size</b></div>
  </header>

  <!-- Front: dog -->
  <section class="flyer flyer--dog">
    <div class="sheet">
      <svg class="bg" viewBox="0 0 895 1268" aria-hidden="true">
        <path d="M440 0 C520 18 570 40 650 62 C770 95 845 190 895 280 L895 0 Z" fill="var(--lilac)"/>
        <path d="M0 88 C40 140 58 200 48 250 C40 300 22 330 0 355" fill="none" stroke="var(--sun)" stroke-width="4"/>
        <path d="M560 660 C515 720 470 800 485 865 C505 950 620 968 705 952 C805 930 845 860 822 760" fill="none" stroke="var(--lilac)" stroke-width="4"/>
        <path d="M0 950 C150 1050 340 1190 480 1268 L0 1268 Z" fill="var(--white)"/>
        <path d="M0 1140 C160 1170 360 1220 515 1268 L0 1268 Z" fill="var(--green)"/>
        <path d="M560 1268 C700 1205 820 1170 895 1185 L895 1268 Z" fill="var(--white)"/>
      </svg>

      <div class="headline headline--top">TOP BENEFITS</div>
      <div class="headline headline--line line-1">OF OUR <strong>PRODUCTS</strong></div>
      <div class="headline headline--line line-2">FOR YOUR</div>
      <div class="headline headline--pet">DOG</div>

      <div class="photo photo--dog-hero" role="img" aria-label="Photo of a brown Labrador sitting in profile"></div>

      <ul class="benefits" style="--badge:var(--lemon);--pad:var(--plum)">
        <li style="top:0"><svg><use href="#paw-badge"/></svg>Supports Healthy Joints &amp; Mobility</li>
        <li style="top:52px"><svg><use href="#paw-badge"/></svg>Promotes A Shiny Coat &amp; Healthy Skin</li>
        <li style="top:105px"><svg><use href="#paw-badge"/></svg>Strengthens Immune System</li>
        <li style="top:157px"><svg><use href="#paw-badge"/></svg>Aids Digestion &amp; Gut Health</li>
        <li style="top:210px"><svg><use href="#paw-badge"/></svg>Boosts Energy &amp; Vitality</li>
        <li style="top:262px"><svg><use href="#paw-badge"/></svg>Reduces Anxiety &amp; Stress</li>
      </ul>

      <div class="frame frame--yellow" role="img" aria-label="Photo of a young man feeding a treat to a dog on grass"></div>
      <div class="frame frame--blue-dog" role="img" aria-label="Photo of a woman brushing a fluffy white dog in a field"></div>
    </div>
  </section>

  <!-- Back: cat -->
  <section class="flyer flyer--cat">
    <div class="sheet">
      <svg class="bg" viewBox="0 0 895 1268" aria-hidden="true">
        <path d="M448 0 C520 20 600 40 690 50 C800 65 860 150 895 270 L895 0 Z" fill="var(--magenta)"/>
        <path d="M740 78 C772 160 790 222 760 282 C700 382 700 452 760 480 C800 496 850 496 895 490" fill="none" stroke="var(--sun)" stroke-width="4"/>
        <ellipse cx="218" cy="768" rx="197" ry="144" fill="none" stroke="var(--lilac)" stroke-width="4"/>
        <path d="M0 1268 C40 1180 120 1140 250 1140 C450 1140 600 1180 720 1100 C800 1050 860 1000 895 950 L895 1268 Z" fill="var(--orange)"/>
        <path d="M380 1268 C500 1222 700 1212 780 1200 C840 1190 880 1170 895 1150 L895 1268 Z" fill="var(--plum)"/>
      </svg>

      <div class="headline headline--top">TOP BENEFITS</div>
      <div class="headline headline--line line-1">OF OUR <strong>PRODUCTS</strong></div>
      <div class="headline headline--line line-2">FOR YOUR</div>
      <div class="headline headline--pet">CAT</div>

      <div class="photo photo--cat-hero" role="img" aria-label="Photo of a tabby kitten sitting with one paw raised"></div>

      <ul class="benefits" style="--badge:var(--royal);--pad:var(--orange)">
        <li style="top:0"><svg><use href="#paw-badge"/></svg>Improves Skin &amp; Coat Health</li>
        <li style="top:56px"><svg><use href="#paw-badge"/></svg>Supports Strong Bones &amp; Joints</li>
        <li style="top:112px"><svg><use href="#paw-badge"/></svg>Enhances Digestive Health</li>
        <li style="top:167px"><svg><use href="#paw-badge"/></svg>Strengthens Immune Function</li>
        <li style="top:223px"><svg><use href="#paw-badge"/></svg>Reduces Hairballs &amp; Shedding</li>
        <li style="top:279px"><svg><use href="#paw-badge"/></svg>Helps Maintain a Healthy Weight</li>
      </ul>

      <div class="frame frame--blue-cat" role="img" aria-label="Photo of a woman offering a treat to a ginger cat on a kitchen counter"></div>
      <div class="photo photo--cats-row" role="img" aria-label="Photo of five cats of different coats sitting in a row"></div>
    </div>
  </section>
</main>
</body>
</html>
```